Webbanner-Design für Slideshow
Zielgruppe
Henrietta bietet 3 Kurse an:
diese Kurse verhelfen einem selbst seine Schutzengel wieder zu hören,
mit ihnen ihren Seelenplan weshalb man auf Erden ist zu sehen,
sowie professionell umzusetzen.
Zielgruppe:
Spirituelle Menschen,
welche Engel lieben,
an sich mental gerne in Kursen & Privat arbeiten,
neues Wissen sich liebend gerne aneignen,
ihren Seelenplan wissen und umsetzen möchten,
die Schönheit im Inneren (Seele) und
im Aussen (Körper & Umgebung) lieben.
Aufgabenstellung
Produktbannerbild für meine Website (Slideshow):
Hintergrund: vorhanden in Form von einem Jpeg, hier auf diesem Foto bitte dich einfach mit folgendem beschäftigen:
Schriftzug groß: Engel (wieder) hören lernen & deinen Seelenplan umsetzen
mit Henrietta Molk (klein, oder großer Schriftzug?)
Schriftzug klein: mehr …
Schriftfarbe: weiss
Schriftart: moderne Schrift (z.Bsp. was die Zeitschriften benützen)
Haus Button Schriftzug: KURSE IN MUC
Buttons Ideen, Vierecke oder Kreise ect.: Transparent bitte und in passender Farbe
Stil: Modern, klar, schön, nicht verschnörkelt, unesoterisch, unverspielt
Mein Logo mit Flügel: irgendwo miteinbauen
Sonstiges: anbei noch ein Iconzeichen für Kurse Seminar
Auflösung Farbe: Text & Icons für Druck (Flyer) & Webproduktpräsentation (Slideshow)
Maße: (bei 1600xca.872 px., bleiben, Banner nicht verkleinern, oder ranzoomen)

```html
<!DOCTYPE html>
<html lang="de">
<head>
<meta charset="utf-8">
<title>Engel hören lernen – Kurse in MUC</title>
<link rel="stylesheet" href="https://fonts.googleapis.com/css2?family=Cinzel:wght@400;500;600;700&display=swap">
<style>
  :root {
    --bg-deep: #bfa2a4;
    --bg-mid: #d8c2c1;
    --bg-light: #ecdedd;
    --photo-white: #f7efee;
    --photo-cream: #efe3e1;
    --photo-rose: #e6cfcd;
    --photo-blush: #dcbcb9;
    --photo-shade: #cdb7b6;
    --text: #ffffff;
  }
  * { margin: 0; padding: 0; box-sizing: border-box; }
  html, body { width: 1200px; height: 654px; overflow: hidden; }
  body { font-family: "Cinzel", "Times New Roman", serif; color: var(--text); }

  .banner {
    position: relative;
    width: 1200px;
    height: 654px;
    overflow: hidden;
    background: linear-gradient(100deg, var(--bg-deep) 0%, var(--bg-mid) 32%, var(--bg-light) 58%, var(--photo-white) 100%);
  }

  .hero-photo {
    position: absolute;
    left: 560px;
    top: 0;
    width: 640px;
    height: 654px;
    background:
      radial-gradient(ellipse 18% 26% at 52% 64%, var(--photo-blush) 0%, rgba(220,188,185,0.6) 60%, rgba(220,188,185,0) 100%),
      radial-gradient(ellipse 10% 10% at 53% 36%, #d9bfb4 0%, rgba(217,191,180,0) 100%),
      radial-gradient(ellipse 14% 14% at 48% 16%, var(--photo-rose) 0%, rgba(230,207,205,0) 100%),
      linear-gradient(180deg, rgba(239,227,225,0) 0%, rgba(239,227,225,0) 55%, var(--photo-cream) 56%, var(--photo-cream) 100%),
      linear-gradient(180deg, rgba(205,183,182,0) 0%, rgba(205,183,182,0) 80%, rgba(205,183,182,0.55) 82%, rgba(205,183,182,0.55) 92%, rgba(205,183,182,0) 93%),
      radial-gradient(ellipse 60% 62% at 58% 46%, var(--photo-white) 0%, var(--photo-cream) 60%, rgba(239,227,225,0) 100%);
    -webkit-mask-image: linear-gradient(90deg, transparent 0%, #000 22%);
    mask-image: linear-gradient(90deg, transparent 0%, #000 22%);
  }

  .brand-mark {
    position: absolute;
    left: 18px;
    top: 60px;
    width: 96px;
    font-size: 16px;
    font-weight: 600;
    letter-spacing: 1.5px;
    text-align: center;
  }

  .headline {
    position: absolute;
    left: 122px;
    top: 44px;
    font-size: 101px;
    font-weight: 600;
    line-height: 1;
    letter-spacing: 0;
  }

  .subline {
    position: absolute;
    left: 21px;
    top: 158px;
    font-size: 41px;
    font-weight: 600;
    line-height: 43px;
    letter-spacing: 0;
  }

  .host {
    position: absolute;
    left: 23px;
    top: 308px;
    font-size: 35px;
    font-weight: 600;
    letter-spacing: 0.5px;
  }

  .more-link {
    position: absolute;
    left: 24px;
    top: 364px;
    font-size: 20px;
    font-weight: 600;
    letter-spacing: 1px;
    color: var(--text);
    text-decoration: none;
  }

  .course-button {
    position: absolute;
    left: 26px;
    top: 524px;
    display: flex;
    align-items: center;
    gap: 20px;
    text-decoration: none;
    color: var(--text);
  }
  .course-button svg { width: 108px; height: 108px; flex: none; }
  .course-button span {
    font-size: 42px;
    font-weight: 600;
    letter-spacing: 0.5px;
  }
</style>
</head>
<body>
  <div class="banner">
    <div class="hero-photo" role="img" aria-label="Foto: Kursleiterin in rosa Bluse am Schreibtisch vor weißem Kamin mit Rosen und Herz-Bilderrahmen, blickt nachdenklich nach oben"></div>

    <div class="brand-mark">Lumara</div>

    <h1 class="headline">ENGEL</h1>
    <p class="subline">(wieder) hören lernen<br>&amp; deinen Seelenplan<br>umsetzen</p>
    <p class="host">mit Henrietta Molk</p>
    <a class="more-link" href="#mehr">mehr …</a>

    <a class="course-button" href="#kurse">
      <svg viewBox="0 0 108 108" aria-hidden="true">
        <circle cx="54" cy="54" r="51" fill="none" stroke="#ffffff" stroke-width="4"/>
        <path d="M54 25 L85 53 L77 53 L77 81 L62 81 L62 63 L46 63 L46 81 L31 81 L31 53 L23 53 Z" fill="#ffffff"/>
        <rect x="69" y="28" width="7" height="14" fill="#ffffff"/>
      </svg>
      <span>kurse in muc</span>
    </a>
  </div>
</body>
</html>
```